Interactive Banner for Maplecrest Elementary School

title :"The Season of Stride”
Slogan: Khao, Khelo, Badho
(Eat, Play, Grow)

Students will place pictures of themselves doing their favorite sport or physical activity so will need space for 200 students.

Banner is around 128 sq feet. Will get exact dimensions.

Banner dimensions Length: 14 ft 9 in Height: 6 ft 9in

The border can be international flags, athletic symbols, etc..

Maybe use watermark athletic symbols in the background

incorporate logo

Target Market(s)

School community and mostly students to bring awareness to a healthy lifestyle

Industry/Entity Type

School

Font styles to use
Serif
Sans Serif

Requirements
Must have
• Space for photograph of children
• "The Season of Stride”
• Khao, Khelo, Badho
• (Eat, Play, Grow)
• Use our color palate listed. see below.
Nice to have
• international flag border

```html
<!DOCTYPE html>
<html lang="en">
<head>
<meta charset="utf-8">
<title>The Season of Stride – Maplecrest Elementary School Banner</title>
<link rel="stylesheet" href="https://fonts.googleapis.com/css2?family=Roboto+Condensed:wght@400;500&display=swap">
<style>
  :root {
    --page-bg: #eceae6;
    --banner-white: #ffffff;
    --grass-light: #b7d38a;
    --grass-mid: #6f9a3e;
    --grass-deep: #3f6a24;
    --band-orange: rgba(214, 78, 52, 0.92);
    --crest-green: #1f4a38;
    --text-white: #ffffff;
    --slot-fill: rgba(255, 255, 255, 0.16);
    --slot-line: rgba(255, 255, 255, 0.7);
  }

  * { box-sizing: border-box; margin: 0; padding: 0; }

  html, body {
    width: 1200px;
    height: 900px;
    overflow: hidden;
    background: var(--page-bg);
  }

  .banner {
    position: absolute;
    left: 50px;
    top: 198px;
    width: 1100px;
    height: 504px;
    overflow: hidden;
    background: var(--banner-white);
    font-family: "Roboto Condensed", "Arial Narrow", sans-serif;
    box-shadow: 0 6px 20px rgba(0, 0, 0, 0.18);
  }

  .banner__photo {
    position: absolute;
    inset: 0;
    background:
      linear-gradient(90deg, #ffffff 0%, rgba(255,255,255,0.95) 18%, rgba(255,255,255,0.55) 34%, rgba(255,255,255,0) 52%),
      linear-gradient(180deg, #d9e6c4 0%, var(--grass-light) 30%, var(--grass-mid) 65%, var(--grass-deep) 100%);
  }

  .school-name {
    position: absolute;
    left: 56px;
    top: 58px;
    display: flex;
    align-items: center;
    gap: 14px;
    color: var(--crest-green);
    font-weight: 500;
    font-size: 26px;
    letter-spacing: 1.5px;
    text-transform: uppercase;
  }

  .school-name__dot {
    width: 22px;
    height: 22px;
    border-radius: 50%;
    background: var(--crest-green);
  }

  .photo-wall {
    position: absolute;
    left: 586px;
    top: 20px;
    width: 490px;
    height: 280px;
  }

  .bands {
    position: absolute;
    inset: 0;
    width: 100%;
    height: 100%;
  }

  .title {
    position: absolute;
    left: 52px;
    top: 386px;
    height: 70px;
    display: flex;
    align-items: center;
    color: var(--text-white);
    font-weight: 400;
    font-size: 56px;
    letter-spacing: -0.5px;
    white-space: nowrap;
  }

  .slogan-local {
    position: absolute;
    left: 588px;
    top: 312px;
    width: 500px;
    height: 36px;
    display: flex;
    align-items: center;
    justify-content: center;
    color: var(--text-white);
    font-weight: 500;
    font-size: 26px;
    letter-spacing: 3px;
    white-space: nowrap;
  }

  .slogan {
    position: absolute;
    left: 588px;
    top: 358px;
    width: 500px;
    height: 64px;
    display: flex;
    align-items: center;
    justify-content: center;
    color: var(--text-white);
    font-weight: 400;
    font-size: 36px;
    letter-spacing: 5px;
    text-transform: uppercase;
    white-space: nowrap;
  }
</style>
</head>
<body>
  <section class="banner">
    <div class="banner__photo" role="img" aria-label="Photograph of children's legs kicking a football across sunlit grass, fading to white on the left"></div>

    <div class="school-name">
      <span class="school-name__dot"></span>
      <span>Maplecrest Elementary School</span>
    </div>

    <svg class="photo-wall" viewBox="0 0 490 280" role="img" aria-label="Space for 200 student photographs, 20 across by 10 down">
      <defs>
        <pattern id="photo-slot" width="24.5" height="28" patternUnits="userSpaceOnUse">
          <rect x="1" y="1" width="22.5" height="26" fill="var(--slot-fill)" stroke="var(--slot-line)" stroke-width="1"/>
        </pattern>
      </defs>
      <rect width="490" height="280" fill="url(#photo-slot)"/>
    </svg>

    <svg class="bands" viewBox="0 0 1100 504" preserveAspectRatio="none" aria-hidden="true">
      <polygon points="0,382 560,382 536,460 0,460" fill="var(--band-orange)"/>
      <polygon points="580,356 1100,356 1100,426 560,426" fill="var(--band-orange)"/>
      <line x1="586" y1="344" x2="548" y2="470" stroke="var(--banner-white)" stroke-width="7"/>
    </svg>

    <h1 class="title">The Season of Stride</h1>
    <p class="slogan-local">Khao, Khelo, Badho</p>
    <p class="slogan">Eat, Play, Grow</p>
  </section>
</body>
</html>
```